Pebble CCTV A5 Flyer for attracting sales

Looking for an A5 flyer to be designed to advertise 3 specific CCTV packages from my website www.pebblecctv.example. the packages are I - 3 camera solution J - 4 cameras and L - 5 cameras. The background of the flyer should be white as I will be printing these myself on standard white A5 paper. Need to advertise also the business contact details and for it to say somewhere "protect your home with our CCTV packages". Also need to get the message across that we supply and install as well as there being a 1 year onsite warranty with all our packages. If you feel A5 is not big enough then feel free to design on A4
Security Service

```html
<!DOCTYPE html>
<html lang="en">
<head>
<meta charset="utf-8">
<title>Pebble CCTV – CCTV Packages Flyer</title>
<link rel="stylesheet" href="https://fonts.googleapis.com/css2?family=Anton&family=Roboto+Condensed:wght@400;700&family=Open+Sans:wght@400;600;700&family=Arimo:wght@400;700&display=swap">
<style>
  :root {
    --orange: #f2873a;
    --yellow: #ffd21f;
    --ink: #333333;
    --dark: #3a3a3a;
    --mist: #ececec;
    --white: #ffffff;
    --red: #e8141c;
    --grey-text: #666666;
    --chip: #d6d6d6;
    --icon: #bbbbbb;
  }
  * { margin: 0; padding: 0; box-sizing: border-box; }
  html, body { width: 849px; height: 1200px; overflow: hidden; background: var(--white); }
  .flyer { position: relative; width: 849px; height: 1200px; overflow: hidden; background: var(--white); font-family: "Open Sans", sans-serif; color: var(--ink); }
  .backdrop { position: absolute; inset: 0; }

  .brand { position: absolute; left: 60px; top: 64px; width: 270px; text-align: center; }
  .brand-name { font-family: "Anton", sans-serif; font-size: 40px; letter-spacing: 0.5px; color: var(--ink); line-height: 1.1; }
  .brand-dot { display: block; margin: 16px auto 0; width: 60px; height: 60px; border-radius: 50%; background: var(--ink); }
  .header-rule { position: absolute; left: 367px; top: 51px; width: 3px; height: 174px; background: #c9c9c9; }
  .headline { position: absolute; left: 418px; top: 68px; font-size: 41px; line-height: 43px; color: var(--ink); font-weight: 400; }
  .headline strong { font-weight: 700; }

  .offer-panel { position: absolute; left: 64px; top: 312px; width: 717px; height: 427px; background: var(--orange); border-radius: 28px 28px 0 0; }
  .promise { position: absolute; left: 64px; top: 348px; width: 717px; text-align: center; font-family: "Roboto Condensed", sans-serif; color: var(--white); font-size: 34px; line-height: 48px; }
  .promise strong { font-weight: 700; }
  .packages-title { position: absolute; left: 64px; top: 466px; width: 717px; text-align: center; font-family: "Anton", sans-serif; font-size: 48px; color: var(--white); text-shadow: 2px 3px 4px rgba(120,50,0,0.5); }

  .package { position: absolute; top: 560px; width: 208px; height: 480px; }
  .package-head { height: 179px; text-align: center; position: relative; }
  .package-code { font-family: "Anton", sans-serif; font-size: 74px; line-height: 1; color: var(--yellow); padding-top: 20px; text-shadow: 2px 3px 0 rgba(120,50,0,0.35); }
  .package-label { font-weight: 700; font-size: 29px; line-height: 31px; color: var(--white); margin-top: 4px; }
  .package-card { position: relative; height: 301px; background: var(--white); border-radius: 0 0 104px 104px; box-shadow: 14px 0 16px -10px rgba(0,0,0,0.25); text-align: center; padding-top: 16px; }
  .card-brandline { display: flex; justify-content: center; align-items: center; gap: 12px; height: 28px; }
  .maker { font-family: "Open Sans", sans-serif; font-weight: 600; font-size: 15px; color: var(--ink); }
  .quality-chip { width: 22px; height: 22px; background: var(--chip); border-radius: 3px; }
  .kit-visual { margin: 8px auto 0; width: 180px; height: 66px; background: linear-gradient(180deg, #e9e9e9 0%, #e9e9e9 55%, #2e2e2e 56%, #2e2e2e 100%); border-radius: 4px; }
  .package-name { font-family: "Arimo", sans-serif; font-size: 19px; line-height: 22px; margin-top: 18px; color: var(--ink); }
  .package-name b { display: block; font-weight: 700; }
  .package-sku { font-family: "Arimo", sans-serif; font-size: 16px; color: var(--grey-text); margin-top: 1px; }
  .package-price { font-family: "Arimo", sans-serif; font-weight: 700; font-size: 16px; margin-top: 22px; color: var(--ink); }

  .promo-sticker { position: absolute; left: 246px; top: 958px; width: 136px; height: 136px; border-radius: 50%; background: var(--red); color: var(--white); text-align: center; transform: rotate(-18deg); font-family: "Arimo", sans-serif; padding-top: 14px; z-index: 5; box-shadow: 2px 3px 6px rgba(0,0,0,0.3); }
  .promo-get { font-size: 17px; color: var(--yellow); }
  .promo-amount { font-size: 27px; font-weight: 700; line-height: 26px; color: var(--yellow); }
  .promo-detail { font-size: 9.5px; line-height: 12px; font-weight: 700; margin-top: 3px; }
  .promo-detail span { color: var(--yellow); }

  .contacts { position: absolute; left: 0; top: 1108px; width: 849px; display: flex; justify-content: center; gap: 18px; color: var(--white); font-size: 16px; align-items: center; white-space: nowrap; }
  .contact { display: flex; align-items: center; gap: 7px; }
  .contact svg { width: 18px; height: 18px; flex: none; }
  .address { position: absolute; left: 0; top: 1146px; width: 849px; text-align: center; color: var(--white); font-size: 17px; display: flex; justify-content: center; align-items: center; gap: 10px; }
  .address strong { font-weight: 700; }
</style>
</head>
<body>
<div class="flyer">
  <svg class="backdrop" width="849" height="1200" viewBox="0 0 849 1200" aria-hidden="true">
    <rect x="-40" y="18" width="890" height="228" rx="114" fill="var(--mist)"/>
    <rect x="40" y="272" width="770" height="34" rx="17" fill="var(--mist)"/>
    <path d="M0 820 Q424 730 849 820 L849 1200 L0 1200 Z" fill="var(--dark)"/>
  </svg>

  <div class="brand">
    <div class="brand-name">Pebble CCTV Ltd</div>
    <span class="brand-dot"></span>
  </div>
  <div class="header-rule"></div>
  <h1 class="headline"><strong>Protect your home</strong><br>with our CCTV<br>packages</h1>

  <div class="offer-panel"></div>
  <p class="promise">we supply and install as well as there being a<br><strong>1 year onsite warranty</strong> with all our packages</p>
  <h2 class="packages-title">Our 3 specific CCTV packages</h2>

  <section class="package" style="left:64px">
    <div class="package-head">
      <div class="package-code">I-3</div>
      <div class="package-label">Camera<br>Solution</div>
    </div>
    <div class="package-card">
      <div class="card-brandline"><span class="maker">Viewpoint</span><span class="quality-chip"></span></div>
      <div class="kit-visual" role="img" aria-label="Three dome cameras above a recorder unit"></div>
      <p class="package-name">(Package I 1080)<b>3 camera<br>CCTV Package<br>Installation</b></p>
      <p class="package-sku">SKU: P0009</p>
      <p class="package-price">£ 609.95</p>
    </div>
  </section>

  <section class="package" style="left:318px">
    <div class="package-head">
      <div class="package-code">J-4</div>
      <div class="package-label">Cameras<br>Solution</div>
    </div>
    <div class="package-card">
      <div class="card-brandline"><span class="maker">Viewpoint</span><span class="quality-chip"></span></div>
      <div class="kit-visual" role="img" aria-label="Four dome cameras above a recorder unit"></div>
      <p class="package-name">(Package J 1080)<b>4 camera<br>CCTV Package<br>Installation</b></p>
      <p class="package-sku">SKU: P0010</p>
      <p class="package-price">£ 659.95</p>
    </div>
  </section>

  <section class="package" style="left:573px">
    <div class="package-head">
      <div class="package-code">L-5</div>
      <div class="package-label">Cameras<br>Solution</div>
    </div>
    <div class="package-card">
      <div class="card-brandline"><span class="maker">Viewpoint</span><span class="quality-chip"></span></div>
      <div class="kit-visual" role="img" aria-label="Five dome cameras above a recorder unit"></div>
      <p class="package-name">(Package L 1080)<b>5 camera<br>CCTV Package<br>Installation</b></p>
      <p class="package-sku">SKU: P0013</p>
      <p class="package-price">£ 759.95</p>
    </div>
  </section>

  <div class="promo-sticker">
    <div class="promo-get">Get</div>
    <div class="promo-amount">£25 off</div>
    <div class="promo-detail">our best-selling<br>4 Camera CCTV Package<br>in January 2018.<br>Use the code <span>JAN25</span><br>at the checkout</div>
  </div>

  <div class="contacts">
    <span class="contact"><svg viewBox="0 0 24 24" fill="none" stroke="var(--icon)" stroke-width="2"><path d="M5 3h4l2 5-2.5 1.5a11 11 0 0 0 6 6L16 13l5 2v4a2 2 0 0 1-2 2A16 16 0 0 1 3 5a2 2 0 0 1 2-2z"/></svg>020 7946 0321</span>
    <span class="contact"><svg viewBox="0 0 24 24" fill="none" stroke="var(--icon)" stroke-width="2"><rect x="2" y="5" width="20" height="14"/><path d="M2 5l10 8 10-8"/></svg>info@pebblecctv.example</span>
    <span class="contact"><svg viewBox="0 0 24 24" fill="none" stroke="var(--icon)" stroke-width="2"><rect x="6" y="2" width="12" height="20" rx="2"/><path d="M11 18h2"/></svg>07700 900 482</span>
    <span class="contact"><svg viewBox="0 0 24 24" fill="none" stroke="var(--icon)" stroke-width="2"><circle cx="12" cy="12" r="10"/><path d="M2 12h20M12 2a15 15 0 0 1 0 20M12 2a15 15 0 0 0 0 20"/></svg>www.pebblecctv.example</span>
  </div>
  <div class="address">
    <svg width="20" height="22" viewBox="0 0 24 26" fill="var(--icon)"><path d="M12 1a8 8 0 0 0-8 8c0 6 8 15 8 15s8-9 8-15a8 8 0 0 0-8-8zm0 11a3 3 0 1 1 0-6 3 3 0 0 1 0 6z"/></svg>
    <span><strong>Pebble CCTV Ltd</strong> 14-16 Harbour Lane, London N1 0ZZ</span>
  </div>
</div>
</body>
</html>
```